Moon River Healing Buisness Cards

I am looking to create a business card for a healing business. In the business I provide coaching and Reiki. I am a licensed LCPC (licensed clinical professional counselor)

Moon River Healing
Soul Centered Healing, Reiki Healinig

Lena Vasquez, L.C.P.C

The card should include the following
biz name: Moon River Healing
my name: Lena Vasquez
website: Lenavasquez.example
email: lena.dorwin@mailbox.example
instagram handle: lenadorwinvasquez

Target Market(s)

Women ages 25-65

```html
<!DOCTYPE html>
<html lang="en">
<head>
<meta charset="utf-8">
<title>Moon River Healing – Business Cards</title>
<link href="https://fonts.googleapis.com/css2?family=Open+Sans:wght@400;600;700&display=swap" rel="stylesheet">
<style>
  :root {
    --backdrop: #666666;
    --card-white: #ffffff;
    --brand-green: #6b9a2a;
    --brand-gold: #d9bc38;
    --ink: #4a4a4a;
  }
  * { margin: 0; padding: 0; box-sizing: border-box; }
  html, body {
    width: 1200px; height: 900px; overflow: hidden;
    background: var(--backdrop);
    font-family: "Open Sans", sans-serif;
  }
  .canvas { position: relative; width: 1200px; height: 900px; }
  .card {
    position: absolute; top: 200px;
    width: 310px; height: 502px;
  }
  .card--front {
    left: 253px; background: var(--card-white);
    border-radius: 60px 0 60px 0;
  }
  .card--back {
    left: 627px; background: var(--brand-green);
    border-radius: 0 60px 0 60px;
  }
  .brand {
    position: absolute; left: 0; right: 0;
    text-align: center;
  }
  .brand__dot {
    display: block; margin: 0 auto;
    border-radius: 50%;
  }
  .brand__name {
    display: block;
    font-weight: 700; font-size: 30px; line-height: 1.15;
    letter-spacing: 0.5px; text-transform: uppercase;
  }
  .card--front .brand { top: 100px; }
  .card--front .brand__dot { width: 56px; height: 56px; background: var(--brand-green); margin-bottom: 22px; }
  .card--front .brand__name { color: var(--brand-green); }
  .card--back .brand { top: 170px; }
  .card--back .brand__dot { width: 90px; height: 90px; background: var(--card-white); margin-bottom: 24px; }
  .card--back .brand__name { color: var(--card-white); }

  .holder {
    position: absolute; left: 32px; top: 359px;
    font-weight: 700; font-size: 20px; letter-spacing: 0.3px;
    text-transform: uppercase; color: var(--brand-green);
  }
  .holder__surname { color: var(--brand-gold); }
  .contacts {
    position: absolute; left: 32px; top: 402px;
    list-style: none; font-size: 14px; line-height: 18.5px; color: var(--ink);
  }
  .contacts li { display: flex; align-items: center; gap: 6px; }
  .contacts svg { width: 12px; height: 12px; flex: none; }

  .services {
    position: absolute; left: 0; right: 0; top: 404px;
    text-align: center; color: var(--card-white);
    font-size: 13px; line-height: 18.5px; text-transform: uppercase;
  }
</style>
</head>
<body>
<main class="canvas">
  <section class="card card--front">
    <div class="brand">
      <span class="brand__dot"></span>
      <span class="brand__name">Moon River<br>Healing</span>
    </div>
    <p class="holder">Lena <span class="holder__surname">Vasquez</span></p>
    <ul class="contacts">
      <li>
        <svg viewBox="0 0 12 12"><rect width="12" height="12" rx="2" fill="#6b9a2a"/></svg>
        lenadorwinvasquez
      </li>
      <li>
        <svg viewBox="0 0 12 12"><circle cx="6" cy="6" r="5.5" fill="#6b9a2a"/><path d="M0.8 6h10.4M6 0.6c-2.6 3-2.6 7.8 0 10.8M6 0.6c2.6 3 2.6 7.8 0 10.8" stroke="#fff" stroke-width="0.9" fill="none"/></svg>
        www.Lenavasquez.example
      </li>
      <li>
        <svg viewBox="0 0 12 12"><rect y="2" width="12" height="8.5" fill="#6b9a2a"/><path d="M0.5 2.5 6 6.8l5.5-4.3" stroke="#fff" stroke-width="1" fill="none"/></svg>
        lena.dorwin@mailbox.example
      </li>
    </ul>
  </section>

  <section class="card card--back">
    <div class="brand">
      <span class="brand__dot"></span>
      <span class="brand__name">Moon River<br>Healing</span>
    </div>
    <p class="services">
      Soul Centered Coaching<br>
      Reiki Healing<br>
      Certified Crystal Reiki Master
    </p>
  </section>
</main>
</body>
</html>
```